Thornbrook MOT Centre Ltd
Unbisased MOT testing.
Thornbrook MOT Centre Ltd - Automotive
Creative Brief
Bright & Fun-filled
Greg Walton plus Tom Hyde (2 sets)
Managing Director plus No title
12 Fernmoor Industrial Park Ashdown Lane (off Brackwell Wharf Lane) Rainham Kent ME8 4TP
info@thornbrookmotcentre.co.uk
www.thornbrookmotcentre.co.uk
Please take a look at leaflet and web sitewe had done and add comments from it if neccessary
Map as per file uploaded and any further comments

```html
<!DOCTYPE html>
<html lang="en">
<head>
<meta charset="utf-8">
<title>Thornbrook MOT Centre Ltd – Stationery</title>
<link href="https://fonts.googleapis.com/css2?family=Roboto+Condensed:wght@400;700&display=swap" rel="stylesheet">
<style>
  :root {
    --stage: #e4e4e4;
    --paper: #ffffff;
    --red: #b3121b;
    --red-dark: #7d0b12;
    --ink: #3a3a3a;
    --muted: #8a8a8a;
    --faint: #f1e3e4;
    --map: #d9d6cf;
    --env-grey: #a3a3a3;
    --env-grey-dark: #6f6f6f;
    --fold: #d4d4d4;
  }
  * { box-sizing: border-box; margin: 0; padding: 0; }
  html, body { width: 1200px; height: 313px; overflow: hidden; }
  body {
    position: relative;
    background: var(--stage);
    font-family: "Roboto Condensed", Arial, sans-serif;
    color: var(--ink);
  }
  .piece {
    position: absolute;
    background: var(--paper);
    box-shadow: 0 1px 4px rgba(0,0,0,.25);
    overflow: hidden;
  }
  .swoosh { position: absolute; left: 0; width: 100%; display: block; }
  .brand {
    position: absolute;
    display: flex; align-items: center; gap: 4px;
    font-weight: 700; color: var(--red); text-transform: uppercase;
    line-height: 1; white-space: nowrap;
  }
  .brand::before { content: ""; width: 1em; height: 1em; background: var(--red); flex: none; }
  .brand--white { color: #fff; }
  .brand--white::before { background: #fff; }
  .watermark { position: absolute; background: var(--faint); }
  .small { position: absolute; font-size: 4px; line-height: 1.35; color: var(--muted); }
  .caption {
    position: absolute; font-size: 6px; color: var(--muted);
    text-align: center;
  }
  .map { position: absolute; background: var(--map); }

  .card { width: 128px; height: 72px; }
  .card--logo { left: 12px; top: 44px; }
  .card--red { left: 12px; top: 118px; background: var(--red); }
  .card--white { left: 146px; top: 118px; }
  .card--map1 { left: 14px; top: 210px; }
  .card--map2 { left: 150px; top: 210px; }

  .letter { width: 172px; height: 244px; }
  .letter--a { left: 283px; top: 28px; }
  .letter--b { left: 482px; top: 24px; }

  .slip { left: 672px; top: 96px; width: 228px; height: 84px; }
  .dl { left: 696px; top: 192px; width: 204px; height: 68px; }

  .envelope { position: absolute; left: 940px; width: 244px; height: 78px; }
  .envelope svg { display: block; width: 100%; height: 100%; }
  .envelope--grey { top: 36px; }
  .envelope--red { top: 120px; }
  .envelope--plain { top: 204px; }
</style>
</head>
<body>

<div class="piece card card--logo">
  <span class="brand" style="left:9px;top:22px;font-size:8px;">Thornbrook MOT Centre</span>
  <svg class="swoosh" style="bottom:0;height:24px" viewBox="0 0 128 24" preserveAspectRatio="none">
    <path d="M0 8 Q64 0 128 6 V24 H0 Z" fill="var(--red)"/>
  </svg>
</div>

<div class="piece card card--red">
  <span class="brand brand--white" style="left:8px;top:8px;font-size:7px;">Thornbrook MOT Centre</span>
  <div class="small" style="left:8px;top:34px;color:#f3d0d2;">
    <strong style="color:#fff">Greg Walton</strong> · Managing Director<br>
    12 Fernmoor Industrial Park, Ashdown Lane<br>
    info@thornbrookmotcentre.co.uk
  </div>
</div>

<div class="piece card card--white">
  <svg class="swoosh" style="top:0;height:14px" viewBox="0 0 128 14" preserveAspectRatio="none">
    <path d="M0 0 H128 V6 Q64 14 0 8 Z" fill="var(--red)"/>
  </svg>
  <span class="brand" style="left:66px;top:22px;font-size:7px;">Thornbrook</span>
  <div class="small" style="left:8px;top:42px;">
    <strong style="color:var(--ink)">Tom Hyde</strong><br>
    Tel 01634 555 010<br>
    www.thornbrookmotcentre.co.uk
  </div>
</div>

<div class="piece card card--map1">
  <div class="map" role="img" aria-label="Location map to the MOT centre" style="inset:4px;"></div>
</div>
<div class="piece card card--map2">
  <div class="map" role="img" aria-label="Location map to the MOT centre" style="left:4px;top:4px;right:40px;bottom:4px;"></div>
  <div style="position:absolute;right:0;top:0;width:36px;height:100%;background:var(--red);"></div>
</div>
<div class="caption" style="left:12px;top:286px;width:266px;">Business Cards</div>

<div class="piece letter letter--a">
  <svg class="swoosh" style="top:0;height:30px" viewBox="0 0 172 30" preserveAspectRatio="none">
    <path d="M0 0 H172 V12 Q90 30 0 18 Z" fill="var(--red)"/>
  </svg>
  <span class="brand" style="left:12px;top:34px;font-size:7px;">Thornbrook MOT Centre</span>
  <div class="watermark" style="left:58px;top:96px;width:56px;height:56px;"></div>
  <div class="small" style="left:12px;right:12px;bottom:8px;text-align:center;">12 Fernmoor Industrial Park Ashdown Lane (off Brackwell Wharf Lane) Rainham Kent ME8 4TP</div>
</div>
<div class="caption" style="left:283px;top:280px;width:172px;">Letterhead</div>

<div class="piece letter letter--b">
  <span class="brand" style="left:12px;top:14px;font-size:7px;">Thornbrook MOT Centre</span>
  <div class="small" style="right:10px;top:12px;text-align:right;">
    12 Fernmoor Industrial Park<br>Ashdown Lane, Rainham<br>Kent ME8 4TP
  </div>
  <div class="watermark" style="left:58px;top:96px;width:56px;height:56px;"></div>
  <svg class="swoosh" style="bottom:0;height:26px" viewBox="0 0 172 26" preserveAspectRatio="none">
    <path d="M0 12 Q90 0 172 10 V26 H0 Z" fill="var(--red)"/>
  </svg>
</div>
<div class="caption" style="left:482px;top:276px;width:172px;">Letterhead</div>

<div class="piece slip">
  <svg class="swoosh" style="top:0;height:22px" viewBox="0 0 228 22" preserveAspectRatio="none">
    <path d="M0 0 H228 V8 Q120 22 0 12 Z" fill="var(--red)"/>
  </svg>
  <span class="brand" style="left:12px;top:26px;font-size:7px;">Thornbrook MOT Centre</span>
  <div class="watermark" style="left:150px;top:30px;width:40px;height:40px;"></div>
</div>
<div class="caption" style="left:672px;top:182px;width:228px;">Compliment Slip</div>

<div class="piece dl">
  <span class="brand" style="left:10px;top:10px;font-size:7px;">Thornbrook MOT Centre</span>
  <svg class="swoosh" style="bottom:0;height:16px" viewBox="0 0 204 16" preserveAspectRatio="none">
    <path d="M0 8 Q110 0 204 6 V16 H0 Z" fill="var(--red)"/>
  </svg>
</div>
<div class="caption" style="left:696px;top:262px;width:204px;">Envelope</div>

<!-- Envelope backs, stacked -->
<div class="piece envelope envelope--grey">
  <svg viewBox="0 0 244 78" preserveAspectRatio="none">
    <rect width="244" height="78" fill="var(--env-grey)"/>
    <path d="M0 78 L122 34 L244 78" fill="none" stroke="#8e8e8e"/>
    <path d="M0 0 H244 L122 46 Z" fill="var(--env-grey-dark)"/>
  </svg>
</div>
<div class="piece envelope envelope--red">
  <svg viewBox="0 0 244 78" preserveAspectRatio="none">
    <rect width="244" height="78" fill="var(--paper)"/>
    <path d="M0 78 L122 36 L244 78" fill="none" stroke="var(--fold)"/>
    <path d="M0 0 H244 L122 42 Z" fill="var(--red)"/>
  </svg>
</div>
<div class="piece envelope envelope--plain">
  <svg viewBox="0 0 244 78" preserveAspectRatio="none">
    <rect width="244" height="78" fill="var(--paper)"/>
    <path d="M0 78 L122 36 L244 78" fill="none" stroke="var(--fold)"/>
    <path d="M0 0 L122 42 L244 0" fill="none" stroke="#c4c4c4"/>
  </svg>
</div>
<div class="caption" style="left:940px;top:288px;width:244px;">Envelopes</div>

</body>
</html>
```